Looking for a website design for my company
Services we offer:
Phone Repair
TV Mounting
Security Camera Installation
Networking / Wi-Fi
Smart Home Services
IT Support

Looking for a website similar to qarnel.com

Few tabs
About Us
Contact Us
Areas Served
Pricing and Services

```html
<!DOCTYPE html>
<html lang="en">
<head>
<meta charset="utf-8">
<title>Vanto Rim – Expert Tech Support</title>
<link href="https://fonts.googleapis.com/css2?family=Roboto:wght@400;500;700&display=swap" rel="stylesheet">
<style>
:root{
  --orange:#f7931e;
  --ink:#2f2f2f;
  --muted:#7a7a7a;
  --line:#d9d9d9;
  --hero-bg:#f2f2f2;
  --dark:#262626;
  --footer:#efefef;
  --bar:#2a2a2a;
  --white:#fff;
}
*{box-sizing:border-box;margin:0;padding:0}
html,body{width:1200px;height:3120px;overflow:hidden}
body{font-family:'Roboto',sans-serif;color:var(--ink);background:var(--white);position:relative}
section,header,footer{position:absolute;left:0;width:1200px}
.abs{position:absolute}
.accent{color:var(--orange)}
p{line-height:1.6}

/* header */
.site-header{top:0;height:60px;background:var(--white)}
.brand{left:110px;top:14px;font-size:30px;font-weight:700;color:var(--ink);display:flex;align-items:center;gap:10px}
.brand-dot{width:14px;height:14px;background:var(--orange)}
.main-nav{right:110px;top:22px;display:flex;gap:30px;font-size:14px;color:var(--ink)}

/* hero */
.hero{top:60px;height:520px;background:var(--hero-bg)}
.hero-photo{left:560px;top:0;width:640px;height:520px;background:linear-gradient(120deg,#e9e9e9 0%,#d8d3cc 45%,#bfb6ab 100%)}
.hero-copy{left:110px;top:120px;width:460px}
.hero-title{font-size:32px;font-weight:700;line-height:1.3}
.hero-text{margin-top:22px;font-size:13px;color:var(--muted);width:380px}
.hero-actions{margin-top:50px;display:flex;gap:22px}
.btn{display:inline-flex;align-items:center;justify-content:center;height:42px;padding:0 26px;border-radius:21px;font-size:14px;font-weight:500}
.btn-primary{background:var(--orange);color:var(--white)}
.btn-outline{border:1.5px solid #bdbdbd;color:var(--ink)}
.slide-arrow{top:240px;width:20px;height:30px}

/* services */
.services{top:630px;height:220px}
.service-list{left:110px;top:0;display:flex;gap:40px}
.service-card{width:130px;height:210px;border:1.5px solid var(--line);border-radius:10px;background:var(--white);display:flex;flex-direction:column;align-items:center;padding-top:40px;box-shadow:0 4px 10px rgba(0,0,0,.06)}
.service-card svg{width:56px;height:56px}
.service-name{margin-top:30px;font-size:12px;text-align:center;line-height:1.4;padding:0 10px}
.service-card.is-active{background:var(--orange);border-color:var(--orange);color:var(--white)}

/* about */
.about{top:960px;height:440px}
.about-photo{left:0;top:0;width:560px;height:440px;background:linear-gradient(135deg,#f4f1ec 0%,#dcd6cf 60%,#c9c0b6 100%)}
.about-copy{left:590px;top:30px;width:500px}
.eyebrow{font-size:15px;font-weight:700;letter-spacing:.5px}
.eyebrow::after{content:"";display:block;width:34px;height:3px;background:var(--orange);margin-top:8px}
.about-title{margin-top:22px;font-size:28px;font-weight:700;line-height:1.35}
.about-text{margin-top:22px;font-size:13px;color:var(--muted)}
.about .btn{margin-top:36px}

/* team */
.team{top:1400px;height:610px;background:linear-gradient(180deg,#3a3a3a,#1f1f1f)}
.section-title{width:100%;text-align:center;font-size:44px;font-weight:700}
.team .section-title{top:80px;color:var(--white)}
.team-member{top:220px;width:280px;text-align:center}
.avatar{width:150px;height:150px;border-radius:50%;margin:0 auto;border:4px solid var(--white);background:linear-gradient(160deg,#9a8f86,#5c544e)}
.member-name{margin-top:24px;font-size:18px;font-weight:500;color:var(--orange)}
.member-bio{margin-top:10px;font-size:12px;color:#cfcfcf;line-height:1.6}

/* contact */
.contact{top:2010px;height:690px;background:var(--white)}
.contact .section-title{top:80px}
.contact-sub{top:160px;width:100%;text-align:center;font-size:13px;color:var(--muted)}
.field{height:42px;border:1px solid var(--line);border-radius:4px;font-size:13px;color:#999;padding:12px 14px;background:var(--white)}
.field-select::after{content:"";position:absolute;right:14px;top:17px;border:5px solid transparent;border-top:6px solid var(--orange)}
.contact .btn{left:535px;top:560px;width:130px}

/* footer */
.site-footer{top:2700px;height:360px;background:var(--footer)}
.footer-brand{left:110px;top:56px;font-size:28px;font-weight:700;display:flex;align-items:center;gap:10px}
.footer-about{left:110px;top:110px;width:300px;font-size:12px;color:var(--muted)}
.footer-heading{font-size:17px;font-weight:700}
.footer-links{left:520px;top:60px}
.footer-links ul{list-style:none;margin-top:18px;font-size:13px;color:var(--muted);line-height:2}
.footer-social{left:735px;top:60px;width:360px}
.subscribe{margin-top:18px;display:flex}
.subscribe-input{width:250px;height:36px;background:var(--white);border:1px solid var(--line);font-size:12px;color:#999;padding:10px 12px}
.subscribe-btn{width:100px;height:36px;background:var(--orange);color:var(--white);font-size:12px;display:flex;align-items:center;justify-content:center}
.social-row{margin-top:22px;display:flex;gap:10px}
.social-dot{width:28px;height:28px;border-radius:50%;background:#555}
.footer-mail{margin-top:14px;font-size:12px;color:var(--muted);display:flex;align-items:center;gap:8px}
.bottom-bar{top:3060px;height:60px;background:var(--bar);color:#cfcfcf;font-size:12px}
.bottom-bar .abs{top:22px}
</style>
</head>
<body>

<header class="site-header">
  <div class="abs brand"><span class="brand-dot"></span>Vanto Rim</div>
  <nav class="abs main-nav"><span>About Us</span><span>Contact Us</span><span>Areas Served</span><span>Pricing and Services</span></nav>
</header>

<section class="hero">
  <div class="abs hero-photo" role="img" aria-label="Technician in a cap installing a smart thermostat on a wall while a homeowner watches"></div>
  <div class="abs hero-copy">
    <h1 class="hero-title">Expert Tech <span class="accent">Support</span> &amp; <span class="accent">Problem</span> Solving In Your Home</h1>
    <p class="hero-text">Lorem ipsum is simply dummy text of the printing and typesetting industry. Lorem ipsum has been the standard dummy text ever since the 1500s, when an unknown printer took a galley.</p>
    <div class="hero-actions"><span class="btn btn-primary">Get In Touch</span><span class="btn btn-outline">Book Services</span></div>
  </div>
  <svg class="abs slide-arrow" style="left:24px" viewBox="0 0 20 30"><path d="M14 5 L5 15 L14 25" fill="none" stroke="#555" stroke-width="3"/></svg>
  <svg class="abs slide-arrow" style="right:24px" viewBox="0 0 20 30"><path d="M6 5 L15 15 L6 25" fill="none" stroke="#555" stroke-width="3"/></svg>
</section>

<section class="services">
  <div class="abs service-list">
    <div class="service-card">
      <svg viewBox="0 0 56 56" fill="none" stroke="#444" stroke-width="2.5"><rect x="16" y="6" width="24" height="44" rx="4"/><line x1="24" y1="44" x2="32" y2="44"/></svg>
      <div class="service-name">Phone<br>Repair</div>
    </div>
    <div class="service-card">
      <svg viewBox="0 0 56 56" fill="none" stroke="#444" stroke-width="2.5"><rect x="8" y="12" width="40" height="26" rx="2"/><line x1="28" y1="38" x2="28" y2="46"/><line x1="18" y1="46" x2="38" y2="46"/></svg>
      <div class="service-name">TV<br>Mounting</div>
    </div>
    <div class="service-card">
      <svg viewBox="0 0 56 56" fill="none" stroke="#444" stroke-width="2.5"><rect x="8" y="16" width="30" height="16" rx="3"/><path d="M38 20 L48 16 L48 32 L38 28"/><line x1="16" y1="32" x2="16" y2="44"/><line x1="10" y1="44" x2="22" y2="44"/></svg>
      <div class="service-name">Security Camera Installation</div>
    </div>
    <div class="service-card">
      <svg viewBox="0 0 56 56" fill="none" stroke="#444" stroke-width="2.5"><path d="M8 22 A28 28 0 0 1 48 22"/><path d="M15 29 A18 18 0 0 1 41 29"/><path d="M22 36 A8 8 0 0 1 34 36"/><circle cx="28" cy="43" r="2.5" fill="#444"/></svg>
      <div class="service-name">Networking /<br>Wi-Fi</div>
    </div>
    <div class="service-card is-active">
      <svg viewBox="0 0 56 56" fill="none" stroke="#fff" stroke-width="2.5"><path d="M8 28 L28 10 L48 28"/><path d="M14 24 V46 H42 V24"/><rect x="24" y="32" width="8" height="14"/></svg>
      <div class="service-name">Smart Home<br>Services</div>
    </div>
    <div class="service-card">
      <svg viewBox="0 0 56 56" fill="none" stroke="#444" stroke-width="2.5"><rect x="8" y="10" width="40" height="28" rx="2"/><line x1="28" y1="38" x2="28" y2="46"/><line x1="18" y1="46" x2="38" y2="46"/><circle cx="28" cy="24" r="6"/></svg>
      <div class="service-name">IT<br>Support</div>
    </div>
  </div>
</section>

<section class="about">
  <div class="abs about-photo" role="img" aria-label="Smiling woman giving two thumbs up in a bright room, framed by an orange diagonal stripe"></div>
  <svg class="abs" style="left:440px;top:0" width="140" height="440" viewBox="0 0 140 440"><polygon points="90,0 120,0 30,440 0,440" fill="var(--orange)"/></svg>
  <div class="abs about-copy">
    <div class="eyebrow">ABOUT US</div>
    <h2 class="about-title">Expert Tech <span class="accent">Support</span> &amp; <span class="accent">Problem</span> Solving In Your Home</h2>
    <p class="about-text">Lorem ipsum is simply dummy text of the printing and typesetting industry. Lorem ipsum has been the industry's standard dummy text ever since the 1500s, when an unknown printer took a galley of type and scrambled it to make a type specimen book. It has survived not only five centuries, but also the leap into electronic typesetting, remaining essentially unchanged.</p>
    <span class="btn btn-primary">Explore &nbsp;›</span>
  </div>
</section>

<section class="team">
  <h2 class="abs section-title">OUR <span class="accent">TEAM</span></h2>
  <div class="abs team-member" style="left:140px">
    <div class="avatar" role="img" aria-label="Portrait of team member Marcus Hale"></div>
    <div class="member-name">Marcus Hale</div>
    <p class="member-bio">Lorem ipsum is simply dummy text of the printing and typesetting industry. Lorem ipsum has been the industry standard.</p>
  </div>
  <div class="abs team-member" style="left:460px">
    <div class="avatar" role="img" aria-label="Portrait of team member Devin Ortiz in a yellow hard hat"></div>
    <div class="member-name">Devin Ortiz</div>
    <p class="member-bio">Lorem ipsum is simply dummy text of the printing and typesetting industry. Lorem ipsum has been the industry standard.</p>
  </div>
  <div class="abs team-member" style="left:780px">
    <div class="avatar" role="img" aria-label="Portrait of team member Liam Porter"></div>
    <div class="member-name">Liam Porter</div>
    <p class="member-bio">Lorem ipsum is simply dummy text of the printing and typesetting industry. Lorem ipsum has been the industry standard.</p>
  </div>
  <svg class="abs slide-arrow" style="left:60px;top:290px" viewBox="0 0 20 30"><path d="M14 5 L5 15 L14 25" fill="none" stroke="#ddd" stroke-width="3"/></svg>
  <svg class="abs slide-arrow" style="right:60px;top:290px" viewBox="0 0 20 30"><path d="M6 5 L15 15 L6 25" fill="none" stroke="#ddd" stroke-width="3"/></svg>
</section>

<section class="contact">
  <h2 class="abs section-title">GET IN <span class="accent">TOUCH</span></h2>
  <p class="abs contact-sub">Lorem ipsum is simply dummy text of the printing and typesetting industry. Lorem</p>
  <div class="abs field" style="left:275px;top:240px;width:310px">First Name</div>
  <div class="abs field" style="left:615px;top:240px;width:310px">Email Address</div>
  <div class="abs field" style="left:275px;top:300px;width:310px">Phone Number</div>
  <div class="abs field field-select" style="left:615px;top:300px;width:310px">Select Service</div>
  <div class="abs field" style="left:275px;top:360px;width:650px;height:140px">Your Message</div>
  <span class="abs btn btn-primary">Submit</span>
</section>

<footer class="site-footer">
  <div class="abs footer-brand"><span class="brand-dot"></span>Vanto Rim</div>
  <p class="abs footer-about">Lorem ipsum is simply dummy text of the printing and typesetting industry. Lorem ipsum has been the industry's standard dummy text ever since the 1500s, when an unknown printer took a galley of type and scrambled it to make a type specimen book. It has survived five centuries and the leap into electronic typesetting.</p>
  <div class="abs footer-links">
    <div class="footer-heading">Quick <span class="accent">Links</span></div>
    <ul><li>About Us</li><li>Contact Us</li><li>Areas Served</li><li>Pricing and Services</li><li>Our Team</li></ul>
  </div>
  <div class="abs footer-social">
    <div class="footer-heading">Stay <span class="accent">Connected</span></div>
    <div class="subscribe"><div class="subscribe-input">Email Address</div><div class="subscribe-btn">Subscribe</div></div>
    <div class="social-row"><span class="social-dot"></span><span class="social-dot"></span><span class="social-dot"></span><span class="social-dot"></span></div>
    <div class="footer-mail"><svg width="16" height="12" viewBox="0 0 16 12" fill="none" stroke="#777" stroke-width="1.4"><rect x="1" y="1" width="14" height="10"/><path d="M1 1 L8 7 L15 1"/></svg>info@vantorim.com</div>
  </div>
</footer>

<div class="abs bottom-bar" style="position:absolute;left:0;width:1200px">
  <span class="abs" style="left:110px">© Vanto Rim 2020</span>
  <span class="abs" style="right:110px">Terms &amp; Conditions &nbsp;|&nbsp; Privacy Policy</span>
</div>

</body>
</html>
```